Package design for quilted mattress covers.

We are producing a comfortable "quilted mattress protector" for beds . We need a very elegant and attractive and cozy insert label. approx. size is 14 inches high x11 inches wide. (One base design with slight edits to customize for each different bed size) It will be packaged in a nice clear bag, with the design label in front. I attached the type of product for reference

package text:
QUILTED MATTRESS COVER

size: 33x75x10"

*ultimate comfort
*breathable cotton top
*waterproof lining
*easy care wash and dry
Updates

Target Market(s)

displayed in drygood and bedding retail stores

Colors

Designer to choose colors to be used in the design.

Requirements
Must have
• all info as in description
Nice to have
• an image of a quilted cover on a bed, professionally included in the package design
Should not have
• ..

```html
<!DOCTYPE html>
<html lang="en">
<head>
<meta charset="utf-8">
<title>Lumora Quilted Mattress Cover – Insert Label</title>
<link rel="stylesheet" href="https://fonts.googleapis.com/css2?family=Comfortaa:wght@300;400;700&family=Archivo+Black&display=swap">
<style>
  :root {
    --navy: #10296b;
    --white: #ffffff;
    --ink: #1a1a1a;
    --cyan: #35c6e6;
    --sky: #4aa3e8;
    --blue: #2a63c9;
    --red: #e8312e;
    --yellow: #f3e63a;
    --green: #7fd14a;
    --magenta: #b2508f;
    --badge-red: #d8261e;
    --photo-light: #f4f5f6;
    --photo-mid: #d9dde0;
  }
  * { margin: 0; padding: 0; box-sizing: border-box; }
  html, body { width: 942px; height: 1200px; overflow: hidden; background: #fff; }
  .label {
    position: relative;
    width: 942px;
    height: 1200px;
    overflow: hidden;
    font-family: "Comfortaa", sans-serif;
  }
  .paint-backdrop {
    position: absolute; inset: 0;
    background:
      radial-gradient(circle at 12% 50%, rgba(232,49,46,.9) 0, rgba(232,49,46,0) 22%),
      radial-gradient(circle at 92% 44%, rgba(232,49,46,.75) 0, rgba(232,49,46,0) 16%),
      radial-gradient(circle at 88% 78%, rgba(243,230,58,.95) 0, rgba(243,230,58,0) 22%),
      radial-gradient(circle at 20% 92%, rgba(127,209,74,.8) 0, rgba(127,209,74,0) 22%),
      radial-gradient(circle at 60% 96%, rgba(53,198,230,.9) 0, rgba(53,198,230,0) 28%),
      radial-gradient(circle at 30% 12%, rgba(74,163,232,.9) 0, rgba(74,163,232,0) 35%),
      linear-gradient(160deg, var(--sky) 0%, var(--cyan) 40%, var(--blue) 70%, var(--cyan) 100%);
  }
  .stripes { position: absolute; inset: 0; }
  .brand {
    position: absolute;
    top: 82px; left: 0; width: 942px;
    text-align: center;
    font-family: "Comfortaa", sans-serif;
    font-weight: 700;
    font-size: 116px;
    line-height: 1;
    color: var(--navy);
    letter-spacing: -2px;
  }
  .product-photo {
    position: absolute;
    left: 173px; top: 306px;
    width: 604px; height: 603px;
    background: linear-gradient(180deg, var(--photo-light) 0%, #e9ecee 45%, var(--photo-mid) 100%);
    box-shadow: 0 0 18px 10px rgba(255,255,255,.95);
  }
  .product-title {
    position: absolute;
    top: 928px; left: 0; width: 942px;
    text-align: center;
    font-family: "Comfortaa", sans-serif;
    font-weight: 400;
    font-size: 58px;
    line-height: 1;
    color: var(--white);
    -webkit-text-stroke: 2px var(--ink);
    letter-spacing: 0;
    white-space: nowrap;
  }
  .features {
    position: absolute;
    left: 40px; top: 1000px;
    width: 413px; height: 177px;
    background: var(--magenta);
    padding: 6px 0 0 10px;
    list-style: none;
    color: var(--white);
    font-size: 28px;
    line-height: 42px;
    font-weight: 400;
  }
  .features li::before { content: "*"; }
  .size-badge {
    position: absolute;
    left: 687px; top: 1110px;
    width: 222px; height: 33px;
    border-radius: 12px;
    background: var(--badge-red);
    color: var(--white);
    font-family: "Archivo Black", sans-serif;
    font-size: 18px;
    line-height: 33px;
    text-align: center;
  }
</style>
</head>
<body>
<main class="label">
  <div class="paint-backdrop" role="img" aria-label="Abstract painted background with sweeping strokes of blue, cyan, red, yellow and green"></div>

  <svg class="stripes" width="942" height="1200" viewBox="0 0 942 1200" aria-hidden="true">
    <g class="stripes-top" fill="#e9fbff" opacity=".85">
      <rect x="0" y="56" width="942" height="8"/>
      <rect x="0" y="78" width="942" height="5"/>
      <rect x="0" y="98" width="942" height="10"/>
      <rect x="0" y="124" width="942" height="6"/>
      <rect x="0" y="146" width="942" height="9"/>
      <rect x="0" y="172" width="942" height="5"/>
      <rect x="0" y="194" width="942" height="8"/>
      <rect x="0" y="218" width="942" height="5"/>
      <rect x="0" y="238" width="942" height="7"/>
    </g>
    <g class="stripes-top-right" stroke="#bff3ff" stroke-width="7" opacity=".7">
      <line x1="700" y1="0" x2="942" y2="140"/>
      <line x1="760" y1="0" x2="942" y2="100"/>
      <line x1="820" y1="0" x2="942" y2="66"/>
      <line x1="640" y1="0" x2="942" y2="180"/>
    </g>
    <g class="stripes-lower-left" stroke="#9be35a" stroke-width="8" opacity=".85">
      <line x1="0" y1="820" x2="240" y2="700"/>
      <line x1="0" y1="860" x2="240" y2="740"/>
      <line x1="0" y1="900" x2="240" y2="780"/>
      <line x1="0" y1="940" x2="240" y2="820"/>
      <line x1="0" y1="980" x2="240" y2="860"/>
      <line x1="0" y1="1020" x2="240" y2="900"/>
    </g>
    <g class="stripes-lower-left-blue" stroke="#2a63c9" stroke-width="5" opacity=".7">
      <line x1="0" y1="840" x2="240" y2="720"/>
      <line x1="0" y1="880" x2="240" y2="760"/>
      <line x1="0" y1="920" x2="240" y2="800"/>
      <line x1="0" y1="960" x2="240" y2="840"/>
    </g>
    <g class="stripes-lower-right" stroke="#e9fbff" stroke-width="6" opacity=".75">
      <line x1="560" y1="1200" x2="942" y2="990"/>
      <line x1="620" y1="1200" x2="942" y2="1030"/>
      <line x1="680" y1="1200" x2="942" y2="1070"/>
      <line x1="500" y1="1200" x2="942" y2="950"/>
    </g>
  </svg>

  <h1 class="brand">Lumora</h1>

  <div class="product-photo" role="img" aria-label="Photo of a white quilted mattress cover on a bed with two white pillows in a bright bedroom"></div>

  <h2 class="product-title">QUILTED MATTRESS COVER</h2>

  <ul class="features">
    <li>ultimate comfort</li>
    <li>breathable cotton top</li>
    <li>waterproof lining</li>
    <li>easy care wash and dry</li>
  </ul>

  <div class="size-badge">size: 33x75x10"</div>
</main>
</body>
</html>
```